Modern Gin Label - Australian Distillery

Kestrel Distillery is working on our first release: Tide Loft Gin, a bold and distinctly Australian small-batch craft gin. We are seeking a professional label design that is modern, fun, and visually highlights our use of unique native botanicals. The label must be print-ready, adhere to Australian spirits labelling regulations, and incorporate room for batch and bottle numbers.
We will be printing a label to go onto the Verolux 700ml Solenne Bottle (VX714K-R), and all files must be prepared to industry standards including dielines, bleed, and print finishes (emboss/foil layers as needed).
________________________________________
Design Objectives
• Modern and Fun: Clean layout, contemporary typefaces, and bright, engaging design
• Botanical-Inspired: Creative use of natural elements or abstract botanical references
• Premium, Craft Feel
• Compliant and Practical: All mandatory label elements included, space for batch/bottle numbers
Bottle & Label Specs (Spec Sheet Attached)
• Bottle: Verolux 700ml Solenne Bottle
o Code: VX714K-R
o Height: 252 ± 1.8 mm
o Diameter: 83.0 ± 1.7 mm
o Label Panel Height: 155.9 mm
** Maximum Label Height 130mm**
o Finish: Cork, 23 mm
• Label Type: Single Front Label up to 2/3 of bottle circumference (preferred) or Front and Back Label
• Logo: To be placed prominently at the top of the label (supplied - resize as apropriate)
Botanical Composition:
Juniper
Coriander Seed
Angelica Root
Lemon Aspen
Desert Lime
Lemon Peel
Mandarin Peel
River Mint
Orris Root
Macadamia Nut
Cassia Bark
Elderflower
Lemon Verbena
Cardamom
Pepperberry
Note: If space or design is tight, designers are encouraged to feature or highlight select botanicals rather than attempt to represent all 15. Interpret botanicals visually, illustratively, texturally, or through abstract form, depending on your creative direction.
Tasting Notes (Optional inclusion – can be used on the back label or subtly featured as a tagline or paragraph - feel free to shorten)
Tasting Notes – Tide Loft Gin
Bright and evocative, Tide Loft Gin opens with a clean, classic juniper backbone. A vibrant citrus medley follows—fresh lemon peel, lemon aspen, and dried mandarin create a layered zestiness, with native desert lime’s tart dryness adding bite. River mint and lemon verbena add herbal lift, with soft floral elderflower and buttery macadamia for depth. A warm spice finish from coriander, cardamom, cassia bark, and pepperberry rounds out this bright, aromatic, and subtly spicy modern Australian gin.
Mandatory Label Inclusions
In compliance with Australian distilled spirits regulations, the label must include:
• Product Name: Tide Loft Gin
• Alcohol Content: 40% ALC/VOL
• Volume: 700 mL
• Standard Drinks: Approx. 22 standard drinks
• Producer Statement:
PRODUCED BY MARLOW PRESSWORKS, 2874 HOLLOWAY CREEK RD, DARLINGTON 5042
FOR KESTREL DISTILLERY
• Country of Origin: Product of Australia
• Pregnancy Warning: Include QRTMB-approved pictogram (Supplied)
• Lot Identification Area:
Provide a blank space marked:
Batch No. ____ | Bottle No. ____
• Barcode (Supplied)
• Allergen Advice (Contains Macadamia Nut)
• Website: kestreldistillery.net.au
Optional Elements (if space and layout permit):
• Short story or brand ethos (can be supplied on request)
• Suggested serve line (e.g., “Ideal for sipping neat, with tonic, or in citrus-forward cocktails.”)
• Craft Distilled icon or statement
• Sober Path Logo – Your Choice (Supplied)
• Recycling Logo
Technical Requirements
• Final Output: Print-ready PDF + native design file (AI preferred)
• Colour Mode: CMYK
• Bleed: 3 mm
• Safe Zone: Clearly defined
• Cut Lines: Clearly marked die line
• Foil: Use spot colour layers for special finishes
• Fonts: Outlined or included in package
• Mock-up: Provide a rendered bottle mock up with applied label
Deliverables
• Front label artwork (and back/wrap if applicable)
• Print-ready PDF
• Adobe Illustrator (or editable vector format) source file
• Separate files or layers for foil/emboss
• Dieline file
• Bottle mockup
NOTES:
1. I have included the QRTMB Standards document for the sizes of the pregnancy logo
2. for the Kestrel Distillery logo, I am happy for you to put a border around it or even use it without the blue background depending on the design.
Target Market(s)
People that are looking for a great tasting Gin, not too serious and loads fun.
Industry/Entity Type
Distilled Spirits
Requirements
Must have
- In compliance with Australian distilled spirits regulations, the label must include: • Product Name: Tide Loft Gin • Alcohol Content: 40% ALC/VOL • Volume: 700 mL • Standard Drinks: Approx. 22 standard drinks • Producer Statement: PRODUCED BY MARLOW PRESSWORKS, 2874 HOLLOWAY CREEK RD, DARLINGTON 5042 FOR KESTREL DISTILLERY • Country of Origin: Product of Australia • Pregnancy Warning: Include QRTMB-approved pictogram (Supplied) • Lot Identification Area: Provide a blank space marked: Batch No. ____ | Bottle No. ____ • Barcode (Supplied) • Allergen Advice (Contains Macadamia Nut) • Website: kestreldistillery.net.au

```html
<!DOCTYPE html>
<html lang="en">
<head>
<meta charset="utf-8">
<title>Tide Loft Gin – Front Label</title>
<link rel="stylesheet" href="https://fonts.googleapis.com/css2?family=Josefin+Sans:wght@700&family=Open+Sans:wght@400&family=Oswald:wght@300;400&display=swap">
<style>
  :root {
    --backdrop: #efedeb;
    --label-paper: #ffffff;
    --ink: #111111;
    --ink-soft: #3a3a3a;
    --gold: #d9a520;
    --leaf: #8fc79a;
    --leaf-deep: #5d9c6c;
    --bloom: #e58bb8;
    --bloom-deep: #c94f8a;
    --lavender: #9aa6dc;
    --field: rgba(255,255,255,0.78);
  }
  html, body {
    margin: 0;
    padding: 0;
    width: 1200px;
    height: 1200px;
    overflow: hidden;
    background: var(--backdrop);
  }
  .label {
    position: absolute;
    left: 220px;
    top: 60px;
    width: 760px;
    height: 1080px;
    background: var(--label-paper);
    overflow: hidden;
    box-shadow: 0 2px 14px rgba(0,0,0,0.08);
  }
  .botanical-art {
    position: absolute;
    left: 0;
    top: 150px;
    width: 760px;
    height: 930px;
    background:
      radial-gradient(ellipse 30% 45% at 12% 55%, rgba(154,166,220,0.55), transparent 70%),
      radial-gradient(ellipse 40% 30% at 60% 45%, rgba(229,139,184,0.55), transparent 70%),
      radial-gradient(ellipse 35% 40% at 90% 55%, rgba(229,139,184,0.45), transparent 70%),
      radial-gradient(ellipse 55% 30% at 50% 80%, rgba(143,199,154,0.7), transparent 75%),
      radial-gradient(ellipse 25% 50% at 6% 60%, rgba(93,156,108,0.55), transparent 70%),
      radial-gradient(ellipse 20% 45% at 96% 35%, rgba(143,199,154,0.5), transparent 70%),
      linear-gradient(to bottom, rgba(255,255,255,0) 0%, rgba(143,199,154,0.15) 40%, rgba(229,139,184,0.25) 100%);
  }
  .brand {
    position: absolute;
    left: 0;
    width: 760px;
    top: 150px;
    display: flex;
    justify-content: center;
    align-items: center;
    gap: 12px;
  }
  .brand-square {
    width: 22px;
    height: 22px;
    background: var(--gold);
  }
  .brand-name {
    font-family: "Open Sans", sans-serif;
    font-weight: 400;
    font-size: 24px;
    color: var(--gold);
    letter-spacing: 0.3px;
  }
  .product-title {
    position: absolute;
    left: 0;
    width: 760px;
    text-align: center;
    font-family: "Josefin Sans", sans-serif;
    font-weight: 700;
    color: var(--ink);
    margin: 0;
  }
  .product-title .line-one {
    position: absolute;
    left: 0;
    width: 760px;
    top: 375px;
    font-size: 84px;
    line-height: 1;
    letter-spacing: -1px;
  }
  .product-title .line-two {
    position: absolute;
    left: 0;
    width: 760px;
    top: 440px;
    font-size: 292px;
    line-height: 1;
    letter-spacing: 4px;
  }
  .lot-field {
    position: absolute;
    top: 898px;
    height: 36px;
    width: 210px;
    background: var(--field);
    font-family: "Oswald", sans-serif;
    font-weight: 400;
    font-size: 22px;
    line-height: 36px;
    color: var(--ink-soft);
    padding-left: 4px;
  }
  .lot-field.batch { left: 138px; }
  .lot-field.bottle { left: 405px; }
  .origin {
    position: absolute;
    left: 135px;
    width: 482px;
    top: 960px;
    display: flex;
    justify-content: space-between;
    font-family: "Oswald", sans-serif;
    font-weight: 300;
    font-size: 26px;
    color: var(--ink-soft);
  }
  .rule {
    position: absolute;
    left: 135px;
    width: 482px;
    top: 1007px;
    height: 2px;
    background: var(--ink-soft);
  }
  .specs {
    position: absolute;
    left: 135px;
    width: 482px;
    top: 1020px;
    display: flex;
    justify-content: space-between;
    font-family: "Oswald", sans-serif;
    font-weight: 400;
    font-size: 22px;
    color: var(--ink-soft);
  }
</style>
</head>
<body>
  <main class="label">
    <div class="botanical-art" role="img" aria-label="Watercolour illustration of native Australian botanicals: rosemary sprigs, blue flowers, pink blossoms and green leaves"></div>

    <div class="brand">
      <span class="brand-square"></span>
      <span class="brand-name">Kestrel Distillery</span>
    </div>

    <h1 class="product-title">
      <span class="line-one">TIDE LOFT</span>
      <span class="line-two">GIN</span>
    </h1>

    <div class="lot-field batch">BATCH#</div>
    <div class="lot-field bottle">BOTTLE#</div>

    <div class="origin" aria-label="Product of Australia">
      <span>P</span><span>R</span><span>O</span><span>D</span><span>U</span><span>C</span><span>T</span>
      <span>&nbsp;</span><span>O</span><span>F</span><span>&nbsp;</span>
      <span>A</span><span>U</span><span>S</span><span>T</span><span>R</span><span>A</span><span>L</span><span>I</span><span>A</span>
    </div>
    <div class="rule"></div>
    <div class="specs">
      <span>40.0% ALC/VOL</span>
      <span>VOL 700ML</span>
    </div>
  </main>
</body>
</html>
```